KP Rubbish Removal Business Card

Hey,
I need a double sided business card designed for a rubbish removal business based in Australia. Logo is already chosen, similar colours preferred for both sides of the business card.

Details to include:

Front:

KP Rubbish Removal
Darren Holloway
Managing Director
Mobile: 0471 920 246
Email: darren@kprubbishremoval.com.au
Website: kprubbishremoval.com.au

Rear:

How did we do?
kprubbishremoval.com.au/review

```html
<!DOCTYPE html>
<html lang="en">
<head>
<meta charset="utf-8">
<title>KP Rubbish Removal – Business Card</title>
<link rel="stylesheet" href="https://fonts.googleapis.com/css2?family=Montserrat:wght@400;500;600;700&display=swap">
<style>
  :root {
    --bg: #d8d8d6;
    --card: #ffffff;
    --green-dark: #17793a;
    --green: #2a9d45;
    --green-lime: #8cc63f;
    --ink: #222222;
    --edge: #1f8c3c;
  }
  * { box-sizing: border-box; margin: 0; padding: 0; }
  html, body {
    width: 1200px; height: 801px; overflow: hidden;
    background: var(--bg);
    font-family: "Montserrat", Arial, sans-serif;
  }
  .stage {
    position: relative; width: 1200px; height: 801px;
    display: flex; align-items: center; justify-content: center; gap: 40px;
  }
  .card {
    position: relative;
    width: 540px; height: 309px;
    background: var(--card);
    border-bottom: 4px solid var(--edge);
    border-right: 2px solid var(--edge);
    box-shadow: 0 14px 30px rgba(0,0,0,0.18);
  }

  /* brand lockup: plain name in the body font, one colour, one weight */
  .brand { display: flex; align-items: center; gap: 14px; }
  .brand-dot {
    width: 46px; height: 46px; border-radius: 50%;
    background: var(--green);
    flex: none;
  }
  .brand-name {
    font-weight: 600; font-size: 24px; line-height: 1;
    color: var(--green-dark);
    white-space: nowrap;
  }

  /* front */
  .card-front .brand { position: absolute; left: 56px; top: 66px; }
  .card-front .info {
    position: absolute; left: 56px; right: 36px; bottom: 64px;
    display: flex; align-items: center;
  }
  .person { flex: none; white-space: nowrap; }
  .person-name {
    font-weight: 700; font-size: 17px; color: var(--green);
    text-transform: uppercase; letter-spacing: 0.3px;
  }
  .person-title { font-size: 12.5px; color: var(--ink); margin-top: 4px; }
  .divider {
    flex: none;
    width: 1px; height: 64px; background: var(--green-lime);
    margin: 0 16px 0 18px;
  }
  .contacts { list-style: none; font-size: 11.5px; color: var(--ink); white-space: nowrap; }
  .contacts li { display: flex; align-items: center; gap: 7px; line-height: 20px; }
  .contacts svg { width: 10px; height: 10px; fill: var(--green); flex: none; }

  /* back */
  .card-back .brand { position: absolute; left: 0; right: 0; top: 78px; justify-content: center; }
  .card-back .brand-dot { width: 64px; height: 64px; }
  .card-back .brand-name { font-size: 28px; }
  .review {
    position: absolute; left: 0; right: 0; bottom: 62px;
    text-align: center; font-size: 14px; color: var(--ink); line-height: 22px;
  }
  .review .domain { color: var(--green); }
</style>
</head>
<body>
<main class="stage">
  <section class="card card-front" aria-label="Business card front">
    <div class="brand">
      <span class="brand-dot"></span>
      <span class="brand-name">KP Rubbish Removal</span>
    </div>
    <div class="info">
      <div class="person">
        <div class="person-name">Darren Holloway</div>
        <div class="person-title">Managing Director</div>
      </div>
      <span class="divider"></span>
      <ul class="contacts">
        <li>
          <svg viewBox="0 0 10 10" aria-hidden="true"><path d="M2 0.5 3.6 2.4 2.7 3.6C3.3 5 4.9 6.6 6.4 7.3L7.6 6.4 9.5 8 8.4 9.5C4.5 9.2 0.8 5.5 0.5 1.6Z"/></svg>
          0471 920 246
        </li>
        <li>
          <svg viewBox="0 0 10 10" aria-hidden="true"><path d="M0.5 2h9v6h-9z M1 2.5 5 5.6 9 2.5" stroke="#fff" stroke-width="0.8"/></svg>
          darren@kprubbishremoval.com.au
        </li>
        <li>
          <svg viewBox="0 0 10 10" aria-hidden="true"><circle cx="5" cy="5" r="4.5"/><path d="M0.5 5h9M5 0.5c-2 2.5-2 6.5 0 9M5 0.5c2 2.5 2 6.5 0 9" stroke="#fff" stroke-width="0.6" fill="none"/></svg>
          www.kprubbishremoval.com.au
        </li>
      </ul>
    </div>
  </section>

  <section class="card card-back" aria-label="Business card back">
    <div class="brand">
      <span class="brand-dot"></span>
      <span class="brand-name">KP Rubbish Removal</span>
    </div>
    <p class="review">
      How did we do?<br>
      www.<span class="domain">kprubbishremoval</span>.com.au/review
    </p>
  </section>
</main>
</body>
</html>
```